Modern Venture Capital website

Design a modern website for a venture capital firm. This website should be modern and beautiful and be on par with other Venture Capital websites. I have a logo and a hero video I'd like to use. Link to hero video: https://files.vantoria.example/f/9Xk2Lm7qPz4Rt8Wb3Nc6Hd5Jy1Gs0Ve/view?ref=share_link

Preference will be given to the best design that combines design with the best images and digital content. That means no generic free stock videos 😅

I currently built a wix website to give you an idea of what content needs to be on the website. Depending on your design it can be 3 pages, or one long page. I will leave it up to you.

WEBSITE: https://brelmor58204.pagecraftly.example/my-site-4

Target Market(s)

Mid-career professionals, individuals interested in Venture Capital

Industry/Entity Type

Finance, venture capital, startups

Requirements
Must have
• must use the hero video I have and must use my logo. Must use high quality images that matches the website design - no generic stock images

```html
<!DOCTYPE html>
<html lang="en">
<head>
<meta charset="utf-8">
<title>Duskline Ventures</title>
<link href="https://fonts.googleapis.com/css2?family=Lato:wght@400;700;900&family=Poppins:wght@300;400;500;600;700&display=swap" rel="stylesheet">
<style>
:root{
  --bg:#141416;
  --bg-deep:#050505;
  --orange:#ff6a2f;
  --white:#ffffff;
  --muted:#d9d9de;
  --lilac:#f0c3ee;
  --line:#3a3a40;
  --ring:#6c4636;
  --ring-fill:#2a1c18;
}
*{box-sizing:border-box;margin:0;padding:0}
html,body{width:1200px;height:2940px;overflow:hidden;background:var(--bg);color:var(--white);font-family:'Poppins',sans-serif}
.page{position:relative;width:1200px;height:2940px}
.abs{position:absolute}
.btn{position:absolute;display:flex;align-items:center;justify-content:center;background:var(--orange);color:var(--white);border-radius:22px;font:600 15px 'Poppins',sans-serif}

/* hero */
.hero{left:0;top:0;width:1200px;height:675px;background:radial-gradient(ellipse at 80% 35%,#5a4330 0%,#2b2622 35%,#15171c 70%),#15171c}
.hero-figure{left:520px;top:90px;width:140px;height:585px;border-radius:60px 60px 0 0;background:linear-gradient(#0b0b0d,#060607);opacity:.85}
.nav{left:59px;top:9px;width:1081px;height:71px;border:1px solid rgba(255,255,255,.28);border-radius:36px}
.brand{left:24px;top:22px;font:700 22px 'Poppins',sans-serif;letter-spacing:-.3px}
.nav-link{top:27px;font:400 13px 'Poppins',sans-serif}
.login{left:843px;top:21px;display:flex;align-items:center;gap:10px;font:500 15px 'Poppins',sans-serif}
.hero-title{left:0;width:1200px;text-align:center}
.hero-title.l1{top:244px;font:300 44px 'Poppins',sans-serif}
.hero-title.l2{top:300px;font:600 44px 'Poppins',sans-serif}
.hero-sub{top:370px;font:400 17px 'Lato',sans-serif}

/* become a vc */
.vc{left:0;top:675px;width:1200px;height:525px;background:radial-gradient(ellipse at 50% 20%,#1c1d24 0%,var(--bg) 60%)}
.h2{left:0;width:1200px;text-align:center;font:700 31px 'Lato',sans-serif}
.lead{left:0;width:1200px;text-align:center;font:400 13px/20px 'Poppins',sans-serif;color:var(--muted)}
.card{top:192px;width:260px;height:259px;border:1px solid var(--line);background:rgba(20,20,24,.6)}
.card::before{content:"";position:absolute;right:-1px;top:-1px;width:50px;height:50px;border-top:2px solid #cfcfd6;border-right:2px solid #cfcfd6}
.card::after{content:"";position:absolute;left:-1px;bottom:-1px;width:50px;height:50px;border-bottom:2px solid #cfcfd6;border-left:2px solid #cfcfd6}
.card.hot{background:var(--orange);border-color:var(--orange)}
.card.hot::before,.card.hot::after{display:none}
.card-icon{position:absolute;left:20px;top:22px;width:54px;height:54px;border-radius:50%;border:1px solid #6a6a72;background:#1d1d22}
.card.hot .card-icon{background:#ff8a5c;border-color:#ffb08e}
.card-rule{position:absolute;left:10px;right:10px;top:94px;height:1px;background:var(--line)}
.card.hot .card-rule{display:none}
.card-title{position:absolute;left:20px;right:16px;font:700 18px/23px 'Lato',sans-serif;color:var(--lilac)}
.card.hot .card-title{color:var(--white)}
.card-text{position:absolute;left:20px;right:22px;font:400 12.5px/19.5px 'Poppins',sans-serif;color:var(--muted)}
.card.hot .card-text{color:#fff3ec}

/* founders */
.founders{left:0;top:1200px;width:1200px;height:420px;background:radial-gradient(ellipse at 60% 30%,#4a3a2e 0%,#2a2420 40%,#161414 80%)}

/* fund */
.fund{left:0;top:1620px;width:1200px;height:387px;background:var(--bg)}
.stat{top:145px;width:230px;text-align:center}
.ring{margin:0 auto;width:102px;height:102px;border-radius:50%;border:1.5px solid var(--ring);background:radial-gradient(circle,#3a241c,var(--ring-fill));display:flex;align-items:center;justify-content:center;font:700 38px 'Lato',sans-serif;color:var(--orange)}
.stat-label{margin-top:14px;font:600 18px/22px 'Poppins',sans-serif;letter-spacing:.4px}

/* cta */
.cta{left:0;top:2007px;width:1200px;height:345px;background:var(--bg-deep)}
.cta-photo{left:0;top:0;width:600px;height:345px;background:radial-gradient(ellipse at 30% 45%,#6a4b2c 0%,#2e241c 45%,#101010 90%)}
.cta-title{left:652px;top:70px;font:600 31px/39px 'Poppins',sans-serif}
.cta-sub{left:652px;top:163px;width:300px;font:400 13px/21px 'Poppins',sans-serif;color:var(--muted)}

/* partners */
.partners{left:0;top:2352px;width:1200px;height:274px;background:var(--bg)}
.partner{top:162px;font:700 22px 'Lato',sans-serif;color:#8a8a90;transform:translateX(-50%);white-space:nowrap}

/* footer */
.footer{left:0;top:2626px;width:1200px;height:314px;background:var(--bg-deep)}
.f-head{top:42px;font:600 18px 'Poppins',sans-serif}
.f-link{font:400 13px 'Poppins',sans-serif;color:var(--muted)}
.f-row{display:flex;align-items:center;gap:14px;font:400 13px/24px 'Poppins',sans-serif;color:var(--muted)}
.f-badge{width:36px;height:36px;border-radius:50%;border:1px solid var(--orange);display:flex;align-items:center;justify-content:center;flex:none}
.f-input{left:607px;top:115px;width:226px;height:42px;border:1px solid #7a7a80;border-radius:21px}
.f-rule{left:62px;top:268px;width:1078px;height:1px;background:var(--line)}
.copy{left:0;top:285px;width:1200px;text-align:center;font:400 12.5px 'Poppins',sans-serif;color:var(--muted)}
</style>
</head>
<body>
<div class="page">

  <section class="abs hero">
    <div class="abs hero-figure" role="img" aria-label="Hero video: a man in a suit looking out over a city skyline at dusk"></div>
    <nav class="abs nav">
      <div class="abs brand">Duskline</div>
      <span class="abs nav-link" style="left:514px">Home</span>
      <span class="abs nav-link" style="left:593px">Join Vc</span>
      <span class="abs nav-link" style="left:672px">Startups</span>
      <div class="abs login">
        <svg width="22" height="22" viewBox="0 0 22 22" fill="none" stroke="#fff" stroke-width="1.5"><circle cx="11" cy="11" r="10"/><circle cx="11" cy="9" r="3.5"/><path d="M4.5 18c1.5-3 4-4 6.5-4s5 1 6.5 4"/></svg>
        Log In
      </div>
      <div class="btn" style="left:931px;top:16px;width:135px;height:40px">Get Started</div>
    </nav>
    <h1 class="abs hero-title l1">Venture Capital for the late night</h1>
    <div class="abs hero-title l2">hustlers</div>
    <p class="abs hero-title hero-sub">Become a Venture Capital Investor</p>
    <div class="btn" style="left:525px;top:419px;width:150px;height:40px">Get Started</div>
  </section>

  <section class="abs vc">
    <h2 class="abs h2" style="top:70px">Become a VC</h2>
    <p class="abs lead" style="top:118px">At Duskline Ventures, we're opening the doors to a new kind of investor, mid-career professionals and<br>aspiring VCs who want real skin in the game, not just exposure from the sidelines.</p>

    <div class="abs card" style="left:59px">
      <div class="card-icon"></div><div class="card-rule"></div>
      <h3 class="card-title" style="top:115px">Hands on VC Work</h3>
      <p class="card-text" style="top:145px">Each Duskline Investor can actively be involved in sourcing, evaluating, and making key investment decisions as little or as much as they want.</p>
    </div>
    <div class="abs card hot" style="left:333px">
      <div class="card-icon"></div>
      <h3 class="card-title" style="top:92px">Meaningful Opportunities to develop your career in Venture Capital</h3>
      <p class="card-text" style="top:165px;right:40px">Duskline Investors, depending on the level of commitment and involvement, can work at our fund as Partners.</p>
    </div>
    <div class="abs card" style="left:607px">
      <div class="card-icon"></div><div class="card-rule"></div>
      <h3 class="card-title" style="top:113px">Earn Carry and Put Your Name on an Investment</h3>
      <p class="card-text" style="top:167px;right:40px">Earn carry interest based on the level of your involvement on each deal.</p>
    </div>
    <div class="abs card" style="left:881px">
      <div class="card-icon"></div><div class="card-rule"></div>
      <h3 class="card-title" style="top:113px;right:60px">Join a community of Hustlers</h3>
      <p class="card-text" style="top:167px">Network with likeminded investors, aspiring investors and limited partners.</p>
    </div>
  </section>

  <section class="abs founders" role="img" aria-label="Photo: silhouette of a founder raising a fist against a dusky sky">
    <h2 class="abs h2" style="top:70px">Simplifying success for founders</h2>
    <p class="abs lead" style="top:126px;left:320px;width:560px;line-height:21px">Our strength lies in our network. Our LPs and operating partners are all mid-to-senior level executives in their industries. They bring real-world corporate experience, offering strategic insights and operational support to help our portfolio companies scale efficiently.</p>
    <p class="abs lead" style="top:218px;line-height:21px">We cut through the noise and get to the core of your business fast.<br>If we love what you're building, we'll move. If not, we'll tell you<br>quickly and respectfully. That lets you make</p>
    <div class="btn" style="left:525px;top:304px;width:150px;height:40px">Learn More</div>
  </section>

  <section class="abs fund">
    <h2 class="abs h2" style="top:70px">Fund Economics</h2>
    <div class="abs stat" style="left:23px"><div class="ring">14</div><div class="stat-label">Pre-Seed / Seed<br>Investments</div></div>
    <div class="abs stat" style="left:255px"><div class="ring">50K</div><div class="stat-label" style="margin-top:20px">Check Size</div></div>
    <div class="abs stat" style="left:485px"><div class="ring">20%</div><div class="stat-label" style="margin-top:20px">Carried Interest</div></div>
    <div class="abs stat" style="left:714px"><div class="ring">2.5%</div><div class="stat-label" style="margin-top:20px">Management Fee</div></div>
    <div class="abs stat" style="left:946px"><div class="ring">1M</div><div class="stat-label" style="margin-top:20px">Fund Size</div></div>
  </section>

  <section class="abs cta">
    <div class="abs cta-photo" role="img" aria-label="Photo: investor working late at a desk in a dim office"></div>
    <h2 class="abs cta-title">Ready to start<br>investing as a VC?</h2>
    <p class="abs cta-sub">Book an interview to learn more and see if you qualify.</p>
    <div class="btn" style="left:651px;top:229px;width:150px;height:40px">Get Started</div>
  </section>

  <section class="abs partners">
    <h2 class="abs h2" style="top:75px">Fund Economics</h2>
    <span class="abs partner" style="left:316px">Harrowfield</span>
    <span class="abs partner" style="left:520px">Tessel Run</span>
    <span class="abs partner" style="left:708px">Quorvia</span>
    <span class="abs partner" style="left:902px">Ambertree</span>
  </section>

  <footer class="abs footer">
    <h4 class="abs f-head" style="left:62px">Links</h4>
    <a class="abs f-link" style="left:62px;top:94px">Solutions</a>
    <a class="abs f-link" style="left:62px;top:125px">Vision</a>
    <a class="abs f-link" style="left:62px;top:156px">Programs</a>
    <a class="abs f-link" style="left:62px;top:187px">Blog</a>

    <h4 class="abs f-head" style="left:335px">Contact Us</h4>
    <div class="abs f-row" style="left:333px;top:86px">
      <span class="f-badge"><svg width="18" height="18" viewBox="0 0 24 24" fill="none" stroke="#ff6a2f" stroke-width="1.6"><path d="M5 3h4l2 5-2.5 1.5a11 11 0 0 0 6 6L16 13l5 2v4a2 2 0 0 1-2 2A17 17 0 0 1 3 5a2 2 0 0 1 2-2z"/></svg></span>
      + 415-555-0182
    </div>
    <div class="abs f-row" style="left:333px;top:138px">
      <span class="f-badge"><svg width="18" height="18" viewBox="0 0 24 24" fill="none" stroke="#ff6a2f" stroke-width="1.6"><rect x="3" y="5" width="18" height="14" rx="2"/><path d="M3 7l9 6 9-6"/></svg></span>
      hello@duskline.example
    </div>
    <div class="abs f-row" style="left:333px;top:190px;align-items:flex-start">
      <span class="f-badge"><svg width="18" height="18" viewBox="0 0 24 24" fill="none" stroke="#ff6a2f" stroke-width="1.6"><path d="M12 22s7-7 7-12a7 7 0 0 0-14 0c0 5 7 12 7 12z"/><circle cx="12" cy="10" r="2.5"/></svg></span>
      <span style="padding-top:8px">218 Larkwood Ave&nbsp; Oakmere,<br>CA 94071</span>
    </div>

    <h4 class="abs f-head" style="left:609px">Our Newsletter</h4>
    <span class="abs f-link" style="left:609px;top:94px">Email *</span>
    <div class="abs f-input"></div>
    <div class="btn" style="left:609px;top:171px;width:135px;height:40px">Submit</div>

    <h4 class="abs f-head" style="left:883px">Follow Us On:</h4>
    <span class="abs f-badge" role="img" aria-label="Social link" style="left:880px;top:93px"></span>
    <span class="abs f-badge" role="img" aria-label="Social link" style="left:923px;top:93px"></span>
    <span class="abs f-badge" role="img" aria-label="Social link" style="left:966px;top:93px"></span>

    <div class="abs f-rule"></div>
    <p class="abs copy">© 2025 duskline ventures. all right reserved.</p>
  </footer>

</div>
</body>
</html>
```